Autodetailing namecard design: Rose Gold Lettering on Black Matt

This is a namecard design project
requiring two-sided design
Base Color of Namecard: black matt

On front:
Company name,
"Lumira Finishes 46 Kenanga"
Subtext: Auto Detailing Studio

Name of card holder: Darren Lim
Phone Number: +6011-4027-8853
address: 46, Jalan Kenanga 5/3Taman Seri Kenanga, 81300 Johor Bahru, Johor, Malaysia

Back:
Our Services
High Gloss Car Paint Protection
Custom Color Modification and Styling
Anti-Chip Glass Protection Film
Heat Rejection Glass Tinting

Target Market(s)

Autodetailing for highend cars

Contact Information for Business Card

as mentioned in project details

Colors

Designer to choose colors to be used in the design.

Requirements
Must have
• The main value-add to this project is the design of a logo suited for our purpose and name, and the inclusion of business card details into the card design

```html
<!DOCTYPE html>
<html lang="en">
<head>
<meta charset="utf-8">
<title>Lumira Finishes 46 Kenanga – Business Card</title>
<link rel="stylesheet" href="https://fonts.googleapis.com/css2?family=Arimo:wght@400&family=Open+Sans:wght@400&display=swap">
<style>
  :root {
    --backdrop: #d9d9db;
    --card-base: #141414;
    --card-base-2: #1c1c1c;
    --card-band: #202020;
    --rose-gold: #d9a08b;
    --rose-gold-deep: #b9786c;
    --rose-light: #ecc9b9;
    --accent-dark: #3a3a3a;
    --accent-grey: #5c5c5c;
  }
  * { margin: 0; padding: 0; box-sizing: border-box; }
  html, body { width: 1200px; height: 864px; overflow: hidden; }
  body {
    background: var(--backdrop);
    position: relative;
    font-family: "Arimo", Arial, sans-serif;
  }
  .card {
    position: absolute;
    width: 560px;
    height: 320px;
    overflow: hidden;
    box-shadow: 0 6px 18px rgba(0,0,0,0.25);
  }

  /* Front side */
  .card-front {
    left: 50px; top: 470px;
    background: linear-gradient(160deg, var(--card-base), var(--card-base-2));
  }
  .front-band {
    position: absolute; left: 0; top: 0; width: 100%; height: 92px;
    background: var(--card-band);
  }
  .front-stripe { position: absolute; }
  .front-stripe.light { left: 0; width: 40%; top: 92px; height: 14px; background: var(--rose-light); }
  .front-stripe.grey  { left: 40%; width: 28%; top: 106px; height: 12px; background: var(--accent-grey); }
  .front-stripe.rose  { left: 68%; width: 32%; top: 118px; height: 12px; background: var(--rose-gold-deep); }
  .company-block {
    position: absolute; right: 36px; top: 20px;
    white-space: nowrap;
  }
  .company {
    font-size: 27px; font-weight: 400; line-height: 1.2;
    color: var(--rose-gold);
  }
  .company-sub {
    padding-left: 30px;
    font-size: 24px; line-height: 1.25;
    color: var(--rose-gold-deep);
  }
  .holder {
    position: absolute; left: 40px; top: 144px;
    font-family: "Open Sans", Arial, sans-serif;
    font-size: 22px; color: var(--rose-gold);
  }
  .contact {
    position: absolute; left: 40px;
    font-family: "Open Sans", Arial, sans-serif;
    font-size: 14px; color: var(--rose-light); line-height: 1.4;
    display: flex; gap: 10px; align-items: flex-start;
  }
  .contact.phone { top: 190px; }
  .contact.address { top: 216px; }
  .contact svg { flex: none; margin-top: 2px; }

  /* Back side */
  .card-back {
    left: 590px; top: 80px;
    background: linear-gradient(160deg, var(--card-base), var(--card-base-2));
  }
  .side-bar { position: absolute; width: 50px; height: 100%; top: 0; }
  .side-bar.left { left: 0; }
  .side-bar.right { right: 0; }
  .side-bar span { display: block; width: 100%; }
  .side-bar .rose  { height: 34%; background: var(--rose-gold-deep); }
  .side-bar .dark  { height: 34%; background: var(--accent-dark); }
  .side-bar .light { height: 32%; background: var(--rose-light); }
  .services {
    position: absolute; left: 50px; right: 50px; top: 92px;
    text-align: center; list-style: none;
    font-size: 19px; color: var(--rose-gold); line-height: 1.4;
  }
</style>
</head>
<body>

  <section class="card card-front" aria-label="Business card front">
    <div class="front-band"></div>
    <div class="front-stripe light"></div>
    <div class="front-stripe grey"></div>
    <div class="front-stripe rose"></div>
    <div class="company-block">
      <h1 class="company">Lumira Finishes 46 Kenanga</h1>
      <p class="company-sub">Auto Detailing Studio</p>
    </div>
    <p class="holder">Darren Lim</p>
    <p class="contact phone">
      <svg width="16" height="16" viewBox="0 0 16 16" aria-hidden="true">
        <rect width="16" height="16" rx="3" fill="var(--rose-gold)"/>
        <path d="M5 4.2c.4-.3.9-.2 1.1.2l.7 1.3c.2.4.1.8-.2 1l-.5.4c.4.9 1 1.6 1.9 2.1l.4-.5c.3-.3.7-.4 1-.2l1.3.7c.4.2.5.7.2 1.1l-.6.7c-.5.5-1.3.6-2 .3C6.4 10.4 5 9 4.3 7.1c-.3-.7-.1-1.5.3-2z" fill="#141414"/>
      </svg>
      <span>+6011-4027-8853</span>
    </p>
    <p class="contact address">
      <svg width="16" height="16" viewBox="0 0 16 16" aria-hidden="true">
        <rect width="16" height="16" rx="3" fill="var(--rose-gold)"/>
        <path d="M8 3a3.3 3.3 0 0 0-3.3 3.3C4.7 8.8 8 13 8 13s3.3-4.2 3.3-6.7A3.3 3.3 0 0 0 8 3zm0 4.6a1.3 1.3 0 1 1 0-2.6 1.3 1.3 0 0 1 0 2.6z" fill="#141414"/>
      </svg>
      <span>46, Jalan Kenanga 5/3Taman Seri Kenanga,<br>81300 Johor Bahru, Johor, Malaysia</span>
    </p>
  </section>

  <section class="card card-back" aria-label="Business card back">
    <div class="side-bar left"><span class="rose"></span><span class="dark"></span><span class="light"></span></div>
    <div class="side-bar right"><span class="rose"></span><span class="dark"></span><span class="light"></span></div>
    <ul class="services">
      <li>Our Services</li>
      <li>High Gloss Car Paint Protection</li>
      <li>Custom Color Modification and Styling</li>
      <li>Anti-Chip Glass Protection Film</li>
      <li>Heat Rejection Glass Tinting</li>
    </ul>
  </section>

</body>
</html>
```